Postcard Design - Thanksgiving Card - Ridgeline Thermal Coils

Here are just a few of the heating and cooling products we offer:

• Steam Coils • Convector Coils
• Hot Water Coils • Re-Heat Coils
• Chilled Water Coils • Tube Bundles
• Direct Expansion (Evaporator) Coils • Shell & Tube Heat Exchangers
• Condensing Coils • Custom Coils to end user spec.’s

ENGINEERING - We can duplicate any existing equipment, even equipment that has been obsolete for years. Ridgeline Thermal personnel will come directly to your job site and match-up dimensions, materials, and performance - all free of charge. We can build from copper, aluminum, cupro-nickel, brass, and more. Heat exchangers and tube bundles can be replaced & warranted as new with great savings; this includes Hart & Pemberly, Wendover-Voss, Lumo, and others. We also make engineering recommendations and suggestions regarding the correct ways to replace equipment or methods of increasing the life expectancy of equipment. We will help solve your HVAC problems, not duplicate them.

```html
<!DOCTYPE html>
<html lang="en">
<head>
<meta charset="utf-8">
<title>Ridgeline Thermal Coils – Thanksgiving Postcard</title>
<link href="https://fonts.googleapis.com/css2?family=Open+Sans:ital,wght@0,400;0,600;1,400&display=swap" rel="stylesheet">
<style>
  :root {
    --page: #ffffff;
    --frame: #c9c9c9;
    --ink: #2b2b2b;
    --card-back: #f6f5f3;
    --card-back-tint: #ebe6e1;
    --photo-sky: #b9c9d6;
    --photo-unit: #8f9598;
    --photo-shirt: #b3282b;
    --band-red: #8e1d20;
    --band-red-dark: #6f1214;
    --footer: #262626;
    --white: #ffffff;
    --shadow: rgba(0,0,0,0.28);
  }
  * { box-sizing: border-box; margin: 0; padding: 0; }
  html, body { width: 1200px; height: 663px; overflow: hidden; }
  body {
    background: var(--page);
    font-family: "Open Sans", Arial, sans-serif;
    color: var(--ink);
    position: relative;
    border: 1px solid var(--frame);
  }
  .card {
    position: absolute;
    top: 126px;
    width: 538px;
    height: 409px;
    box-shadow: 0 1px 6px var(--shadow);
    overflow: hidden;
  }

  /* ---------- Back side ---------- */
  .card--back { left: 50px; background: var(--card-back); }
  .card--back .backdrop {
    position: absolute; inset: 0;
    background: linear-gradient(135deg, var(--card-back) 0%, var(--card-back-tint) 55%, var(--card-back) 100%);
    opacity: .8;
  }
  .brand {
    position: absolute;
    display: flex; align-items: center; gap: 6px;
    font-weight: 600; color: var(--ink);
    line-height: 1.15;
  }
  .brand__mark { width: 12px; height: 12px; background: var(--ink); flex: none; }
  .card--back .brand { left: 32px; top: 42px; width: 100px; font-size: 12px; }
  .contact {
    position: absolute; left: 141px; top: 36px;
    font-size: 12.5px; line-height: 18px;
  }
  .contact__line { display: flex; align-items: center; gap: 6px; }
  .contact__line svg { width: 11px; height: 11px; fill: var(--ink); }
  .products {
    position: absolute; left: 33px; top: 138px;
    font-size: 10px; line-height: 12.6px;
  }
  .products__title { margin-bottom: 2px; }
  .products__list { padding-left: 30px; font-size: 8.6px; }
  .products__list li { line-height: 12.3px; }
  .products__extra { margin-top: 2px; }

  /* ---------- Front side ---------- */
  .card--front { left: 610px; background: var(--band-red); }
  .hero {
    position: absolute; left: 0; top: 0; width: 538px; height: 243px;
    background: linear-gradient(100deg, var(--photo-sky) 0%, var(--photo-unit) 45%, var(--photo-shirt) 72%, #3c3f45 100%);
  }
  .card--front .brand {
    left: 31px; top: 22px; width: 136px; height: 51px;
    background: var(--white); padding: 0 10px; font-size: 12px;
  }
  .band {
    position: absolute; left: 0; top: 243px; width: 538px; height: 127px;
    background: linear-gradient(180deg, var(--band-red) 0%, var(--band-red-dark) 100%);
    color: var(--white);
  }
  .band__title {
    position: absolute; left: 31px; top: 14px;
    font-size: 27px; font-weight: 400; letter-spacing: .5px;
  }
  .band__body { position: absolute; left: 31px; top: 54px; width: 338px; font-size: 8px; line-height: 10.6px; }
  .band__body p + p { margin-top: 9px; text-align: justify; }
  .band__sign { position: absolute; right: 175px; top: 111px; font-size: 7.5px; font-style: italic; }
  .inset {
    position: absolute; left: 376px; top: 210px; width: 143px; height: 161px;
    background: var(--white); padding: 5px;
  }
  .inset__photo {
    width: 100%; height: 100%;
    background: linear-gradient(160deg, #c7ccd0 0%, #7e8b8f 45%, #5c7fa6 70%, #d9d5cc 100%);
  }
  .footer {
    position: absolute; left: 0; top: 370px; width: 538px; height: 39px;
    background: var(--footer); color: var(--white);
    display: flex; align-items: center; padding: 0 20px 0 30px; gap: 22px;
  }
  .footer__address { font-size: 9.5px; }
  .footer__phone { font-size: 15px; display: flex; align-items: center; gap: 4px; }
  .footer__email { font-size: 12px; display: flex; align-items: center; gap: 5px; margin-left: auto; }
  .footer svg { width: 10px; height: 10px; fill: var(--white); }
</style>
</head>
<body>

<section class="card card--back">
  <div class="backdrop" role="img" aria-label="Faded photo of copper coil bundles"></div>
  <div class="brand"><span class="brand__mark"></span>Ridgeline Thermal Coils</div>
  <div class="contact">
    <div>P. O. Box 2875</div>
    <div>Fernbrook, MI 48092</div>
    <div class="contact__line"><svg viewBox="0 0 12 12"><path d="M1 4c0-2 2-3 5-3s5 1 5 3v1H8V4H4v1H1zM2 6h8l1 5H1z"/></svg>888-555-0147</div>
    <div class="contact__line"><svg viewBox="0 0 12 12"><path d="M1 2h10v8H1zM1 2l5 4 5-4" stroke="#f6f5f3" stroke-width="1"/></svg>coilteam@ridgelinemail.net</div>
  </div>
  <div class="products">
    <div class="products__title">Heating and cooling products</div>
    <ul class="products__list">
      <li>Steam Coils</li>
      <li>Convector Coils</li>
      <li>Hot Water Coils</li>
      <li>Re-Heat Coils</li>
      <li>Chilled Water Coils</li>
      <li>Tube Bundles</li>
      <li>Direct Expansion (Evaporator) Coils</li>
      <li>Shell &amp; Tube Heat Exchangers</li>
      <li>Condensing Coils</li>
      <li>Custom Coils to end user spec.’s</li>
    </ul>
    <div class="products__extra">Duplicate any existing equipment</div>
    <div>Engineering recommendations and suggestions</div>
  </div>
</section>

<section class="card card--front">
  <div class="hero" role="img" aria-label="Photo of two HVAC technicians in hard hats servicing a rooftop condenser unit"></div>
  <div class="brand"><span class="brand__mark"></span>Ridgeline Thermal Coils</div>
  <div class="band">
    <h1 class="band__title">HAPPY THANKSGIVING!</h1>
    <div class="band__body">
      <p>It is the time of year for remembering everything that makes us grateful.</p>
      <p>That is why we want to express our appreciation for your confidence in our firm to assist you on your jobsite or at your facility to solve a coil or heat exchanger problem.</p>
    </div>
    <div class="band__sign">Dale Renner &amp; Gus Holloway</div>
  </div>
  <div class="inset"><div class="inset__photo" role="img" aria-label="Photo of a technician testing equipment on site"></div></div>
  <div class="footer">
    <span class="footer__address">P. O. Box 2875 Fernbrook, MI 48092</span>
    <span class="footer__phone"><svg viewBox="0 0 12 12"><path d="M1 4c0-2 2-3 5-3s5 1 5 3v1H8V4H4v1H1zM2 6h8l1 5H1z"/></svg>888-555-0147</span>
    <span class="footer__email"><svg viewBox="0 0 12 12"><path d="M1 2h10v8H1zM1 2l5 4 5-4" stroke="#262626" stroke-width="1"/></svg>coilteam@ridgelinemail.net</span>
  </div>
</section>

</body>
</html>
```